Kitchen Renovation in YOUR area

We need a template for a flyer that we can hand out in neighbourhoods when we're finished renovating a kitchen. Every neighbourhood, we'll swap out a before and after picture to personalize to that neighbourhood. These will be low print run flyers (30-50 each time). We're really hoping that they'll see *their* kitchen in the BEFORE section (since many houses in neighbourhoods are similar) and see what they're kitchen could look like in the AFTER section. So I want the BEFORE and AFTER photos to be easily swapped in and out on my end. I have lots of photos if needed.

Target Market(s)

Home owners looking to have their kitchen's renovated. This is typically in the 35-55 age range. Primarily women.

Colors

Designer to choose colors to be used in the design.

Requirements
Must have
• My logo, a before (0962) and an after (8281) that I can swap out as I go from neighborhood to neighborhood. All the other design elements can be permanent.
• My website address: MaplestoneRemodels.com
Nice to have
• A background of some kitchen work I've done (1171.jpg). I've also included some copy. That copy can change - that's just something I did up quickly. Use what you can and I can make changes later

```html
<!DOCTYPE html>
<html lang="en">
<head>
<meta charset="utf-8">
<title>Maplestone Remodels – Kitchen Refacing Flyer</title>
<link href="https://fonts.googleapis.com/css2?family=Oswald:wght@300;500;600&family=Source+Sans+3:wght@400;600;700&display=swap" rel="stylesheet">
<style>
  :root{
    --blue:#0d64a6;
    --blue-dark:#0b5591;
    --ink:#1c1c1c;
    --grey-text:#5a5b5d;
    --panel:#e3e3e5;
    --footer:#2a2a2b;
    --white:#ffffff;
    --stage:#7b7b7c;
  }
  *{box-sizing:border-box;margin:0;padding:0}
  html,body{width:1200px;height:1200px;overflow:hidden;background:var(--stage)}
  .stage{position:relative;width:1200px;height:1200px;overflow:hidden}
  .flyer{
    position:absolute;left:159px;top:30px;width:1037px;height:1341px;
    transform:scale(.85);transform-origin:0 0;background:var(--white);
    box-shadow:0 10px 40px rgba(0,0,0,.35);overflow:hidden;
    font-family:"Source Sans 3",sans-serif;color:var(--ink);
  }
  .brand{position:absolute;left:34px;top:70px;display:flex;align-items:center;gap:14px}
  .brand-mark{width:26px;height:26px;background:var(--blue)}
  .brand-name{font-weight:700;font-size:44px;line-height:1;color:var(--grey-text);letter-spacing:.5px}
  .web-bar{position:absolute;left:562px;top:82px;width:475px;height:52px}
  .web-bar > .web-shape{position:absolute;left:0;top:0}
  .web-text{position:absolute;left:90px;top:0;height:52px;display:flex;align-items:center;gap:10px;
    color:var(--white);font-weight:700;font-size:28px;white-space:nowrap}
  .web-icon{flex:none}
  .hero{position:absolute;left:0;top:214px;width:1037px;height:350px;
    background:linear-gradient(100deg,#6e6f73 0%,#a9abaf 30%,#d9dadc 60%,#f1f1f2 100%)}
  .hero-banner{position:absolute;left:0;top:350px;width:580px;height:194px}
  .hero-title{position:absolute;left:32px;top:370px;color:var(--white);white-space:nowrap;
    font-family:"Oswald",sans-serif;font-weight:600;font-size:56px;line-height:1;letter-spacing:-.5px}
  .hero-sub{position:absolute;left:32px;top:440px;color:var(--white);
    font-family:"Oswald",sans-serif;font-weight:300;font-size:34px;line-height:40px}
  .hero-note-box{position:absolute;left:505px;top:482px;width:532px;height:82px}
  .hero-note{position:absolute;left:540px;top:508px;width:480px;text-align:center;
    font-size:20px;font-weight:600;line-height:26px}
  .intro-panel{position:absolute;left:0;top:600px;width:1037px;height:356px}
  .intro-text{position:absolute;left:46px;top:622px;width:955px;font-size:26px;font-weight:600;
    line-height:33px;text-align:justify;text-align-last:left;text-indent:49px;hyphens:auto}
  .gallery{position:absolute;left:30px;top:748px;display:flex;gap:5px}
  .card{position:relative;width:240px;height:175px}
  .card svg{position:absolute;left:0;top:0}
  .card-label{position:absolute;left:0;right:12px;bottom:8px;text-align:center;
    color:var(--blue);font-weight:700;font-size:22px;letter-spacing:.3px}
  .divider{position:absolute;left:414px;top:965px}
  .copy{position:absolute;top:1000px;font-size:25px;font-weight:600;line-height:32.5px;hyphens:auto}
  .copy-left{left:35px;width:524px;text-align:justify;text-align-last:left}
  .copy-right{left:594px;width:406px;text-align:justify;text-align-last:left}
  .accent{color:var(--blue)}
  .footer-shape{position:absolute;left:0;top:1214px}
  .contact-head{position:absolute;left:33px;top:1240px;color:var(--white)}
  .contact-head strong{display:block;font-size:33px;font-weight:700;line-height:38px}
  .contact-head span{display:block;font-size:29px;font-weight:600;line-height:36px}
  .contact-item{position:absolute;top:1280px;display:flex;align-items:center;gap:8px;
    color:var(--white);font-weight:700;white-space:nowrap}
  .contact-phone{left:360px;font-size:29px}
  .contact-email{left:606px;font-size:26px}
</style>
</head>
<body>
<div class="stage">
  <article class="flyer">

    <header>
      <div class="brand">
        <span class="brand-mark"></span>
        <span class="brand-name">Maplestone Remodels</span>
      </div>
      <div class="web-bar">
        <svg class="web-shape" width="475" height="52" viewBox="0 0 475 52">
          <polygon points="20,0 36,0 16,52 0,52" fill="var(--blue)"/>
          <polygon points="44,0 60,0 40,52 24,52" fill="var(--blue)"/>
          <polygon points="62,52 82,0 475,0 475,52" fill="var(--footer)"/>
        </svg>
        <div class="web-text">
          <svg class="web-icon" width="18" height="18" viewBox="0 0 18 18" fill="none" stroke="#fff" stroke-width="1.6">
            <circle cx="9" cy="9" r="7.5"/><ellipse cx="9" cy="9" rx="3.2" ry="7.5"/>
            <line x1="1.5" y1="9" x2="16.5" y2="9"/>
          </svg>
          <span>MaplestoneRemodels.com</span>
        </div>
      </div>
    </header>

    <section class="hero-section">
      <div class="hero" role="img" aria-label="Photo of a finished white kitchen with mosaic tile backsplash and stone counters"></div>
      <svg class="hero-banner" width="580" height="194" viewBox="0 0 580 194">
        <polygon points="0,0 572,0 498,194 0,194" fill="var(--blue)"/>
      </svg>
      <h1 class="hero-title">Maplestone Remodels</h1>
      <p class="hero-sub">Turn your kitchen into your dream<br>kitchen by refacing</p>
      <svg class="hero-note-box" width="532" height="82" viewBox="0 0 532 82">
        <polygon points="30,12 532,12 532,82 0,82" fill="var(--white)"/>
        <polygon points="45,0 532,0 532,12 40,12" fill="var(--blue)"/>
      </svg>
      <p class="hero-note">We've just completed a kitchen refacing in your area—and the results are stunning. Take a look!</p>
    </section>

    <section class="results">
      <svg class="intro-panel" width="1037" height="356" viewBox="0 0 1037 356">
        <polygon points="50,0 1037,0 1037,356 0,356 0,48" fill="var(--panel)"/>
      </svg>
      <p class="intro-text">A kitchen refacing takes much less time, and costs up to 60% less than a full kitchen renovation. Get the kitchen you always dreamed of without all of the disruption of a full renovation.</p>

      <div class="gallery">
        <figure class="card">
          <svg width="240" height="175" viewBox="0 0 240 175" role="img" aria-label="Before photo: dated kitchen with oak cabinets and stainless fridge">
            <defs><linearGradient id="before-a" x1="0" y1="0" x2="1" y2="1"><stop offset="0" stop-color="#8a5a34"/><stop offset="1" stop-color="#3a2a22"/></linearGradient></defs>
            <polygon points="20,62 238,62 220,173 2,173" fill="none" stroke="#6d6e70" stroke-width="1.5"/>
            <polygon points="42,2 238,2 216,130 24,130" fill="url(#before-a)" stroke="var(--blue)" stroke-width="4"/>
          </svg>
          <figcaption class="card-label">BEFORE</figcaption>
        </figure>
        <figure class="card">
          <svg width="240" height="175" viewBox="0 0 240 175" role="img" aria-label="After photo: refaced kitchen with white cabinets and stainless appliances">
            <defs><linearGradient id="after-a" x1="0" y1="0" x2="1" y2="1"><stop offset="0" stop-color="#f2f2f0"/><stop offset=".6" stop-color="#c9c9c7"/><stop offset="1" stop-color="#a2764c"/></linearGradient></defs>
            <polygon points="20,62 238,62 220,173 2,173" fill="none" stroke="#6d6e70" stroke-width="1.5"/>
            <polygon points="42,2 238,2 216,130 24,130" fill="url(#after-a)" stroke="var(--blue)" stroke-width="4"/>
          </svg>
          <figcaption class="card-label">AFTER</figcaption>
        </figure>
        <figure class="card">
          <svg width="240" height="175" viewBox="0 0 240 175" role="img" aria-label="Before photo: dated kitchen with oak cabinets and stainless fridge">
            <defs><linearGradient id="before-b" x1="0" y1="0" x2="1" y2="1"><stop offset="0" stop-color="#8a5a34"/><stop offset="1" stop-color="#3a2a22"/></linearGradient></defs>
            <polygon points="20,62 238,62 220,173 2,173" fill="none" stroke="#6d6e70" stroke-width="1.5"/>
            <polygon points="42,2 238,2 216,130 24,130" fill="url(#before-b)" stroke="var(--blue)" stroke-width="4"/>
          </svg>
          <figcaption class="card-label">BEFORE</figcaption>
        </figure>
        <figure class="card">
          <svg width="240" height="175" viewBox="0 0 240 175" role="img" aria-label="After photo: refaced kitchen with white cabinets and stainless appliances">
            <defs><linearGradient id="after-b" x1="0" y1="0" x2="1" y2="1"><stop offset="0" stop-color="#f2f2f0"/><stop offset=".6" stop-color="#c9c9c7"/><stop offset="1" stop-color="#a2764c"/></linearGradient></defs>
            <polygon points="20,62 238,62 220,173 2,173" fill="none" stroke="#6d6e70" stroke-width="1.5"/>
            <polygon points="42,2 238,2 216,130 24,130" fill="url(#after-b)" stroke="var(--blue)" stroke-width="4"/>
          </svg>
          <figcaption class="card-label">AFTER</figcaption>
        </figure>
      </div>
    </section>

    <svg class="divider" width="512" height="12" viewBox="0 0 512 12">
      <polygon points="10,0 502,0 512,12 0,12" fill="var(--blue-dark)"/>
    </svg>

    <section class="benefits">
      <p class="copy copy-left">Refacing is a complete kitchen facelift. Replace the doors (and the out-dated style!), trim, and panels and pick something new and fresh. Make any modifications you'd like (is it time to switch that junk cabinet into a pot-and-pan cabinet?).</p>
      <p class="copy copy-right">Less mess <span class="accent">(no need to empty cupboards)</span>, less cost (save up to 60% of a typical kitchen renovation), save time <span class="accent">(a kitchen refacing typically takes only 3 days!)</span></p>
    </section>

    <footer>
      <svg class="footer-shape" width="1037" height="127" viewBox="0 0 1037 127">
        <polygon points="0,0 305,0 330,27 1037,27 1037,127 0,127" fill="var(--footer)"/>
        <polygon points="328,2 1037,2 1037,14 340,14" fill="var(--blue)"/>
      </svg>
      <div class="contact-head">
        <strong>Contact Us</strong>
        <span>For More Information</span>
      </div>
      <div class="contact-item contact-phone">
        <svg width="12" height="20" viewBox="0 0 12 20"><rect x="1" y="1" width="10" height="18" rx="2" fill="none" stroke="var(--blue)" stroke-width="2"/><rect x="4" y="15" width="4" height="2" fill="var(--blue)"/></svg>
        555-214-7830
      </div>
      <div class="contact-item contact-email">
        <svg width="16" height="12" viewBox="0 0 16 12"><rect x="0" y="0" width="16" height="12" fill="var(--blue)"/><polyline points="0,0 8,7 16,0" fill="none" stroke="var(--footer)" stroke-width="1.4"/></svg>
        Dana@MaplestoneRemodels.com
      </div>
    </footer>

  </article>
</div>
</body>
</html>
```